Lawn Sign Design

I'm looking for a new lawn sign design to help promote our landscape company. We're trying to position ourselves as a leader in our market, so obviously quality and elegance are important to us.

Phone Number: (555) 214-3098
Website: verdalquix.com
Our tagline: "Your hands are full... Let us help"

Full Service
Weekly Sawn Service
Lanscape Lighting
Spring/Fall Clean Ups
Turf Edging
Snow Removal

I have attached a jpg of our logo to help with design colors. I will provide the vector file upon completion of this project.

Feel free to use your imagination. I know little about content of effective lawn signs, so I'm relying a lot on you, the professionals.

Thanks
Updates

Project Deadline Extended
Reason: Haven't found what I'm looking for.

Industry/Entity Type

Landscape

Requirements
Must have
• Class, elegance, professionalism.
Should not have
• Tacky cartoonish looking desings

```html
<!DOCTYPE html>
<html lang="en">
<head>
<meta charset="utf-8">
<title>Verdal Lawn Flyer</title>
<link href="https://fonts.googleapis.com/css2?family=Montserrat:wght@400;600;700;800&display=swap" rel="stylesheet">
<style>
  :root {
    --page-bg: #e6e5e1;
    --paper: #ffffff;
    --green-deep: #1f4d1c;
    --green-mid: #2e6b22;
    --green-bright: #5a9e2c;
    --orange: #f2661c;
    --ink: #111111;
    --tagline: #2a4a22;
  }
  html, body {
    margin: 0;
    width: 1200px;
    height: 1000px;
    overflow: hidden;
    background: var(--page-bg);
  }
  .flyer {
    position: absolute;
    left: 260px;
    top: 20px;
    width: 680px;
    height: 960px;
    box-shadow: 0 6px 24px rgba(0,0,0,.18);
  }
  .flyer svg { display: block; }
  .brand-title { font: 800 112px "Montserrat", sans-serif; fill: var(--ink); letter-spacing: -2px; }
  .brand-mark-name { font: 800 15px "Montserrat", sans-serif; fill: var(--ink); }
  .tagline { font: 400 27px "Montserrat", sans-serif; fill: var(--tagline); letter-spacing: .5px; }
  .service { font: 600 25px "Montserrat", sans-serif; fill: var(--orange); }
  .service-icon circle { fill: var(--paper); stroke: var(--ink); stroke-width: 2; }
  .service-icon path { fill: var(--ink); }
  .phone { font: 700 40px "Montserrat", sans-serif; fill: var(--orange); }
  .website { font: 400 30px "Montserrat", sans-serif; fill: #ffffff; }
</style>
</head>
<body>
<div class="flyer">
  <svg width="680" height="960" viewBox="0 0 680 960">
    <defs>
      <linearGradient id="houseSceneTone" x1="0" y1="0" x2="0" y2="1">
        <stop offset="0" stop-color="#dfe6ea"/>
        <stop offset=".45" stop-color="#c9d2d0"/>
        <stop offset=".62" stop-color="#6fa23a"/>
        <stop offset="1" stop-color="#3f8a1f"/>
      </linearGradient>
      <linearGradient id="lightingSceneTone" x1="0" y1="0" x2="1" y2="1">
        <stop offset="0" stop-color="#9a9c96"/>
        <stop offset=".55" stop-color="#c8c3b2"/>
        <stop offset="1" stop-color="#6b8d3a"/>
      </linearGradient>
    </defs>

    <rect class="paper" width="680" height="960" fill="var(--paper)"/>

    <g class="hero-photo" role="img" aria-label="Photo of white suburban houses with a green manicured lawn and hedges">
      <rect width="680" height="560" fill="url(#houseSceneTone)"/>
    </g>

    <path class="wave-band-top" d="M0,20 C180,0 420,-10 680,0 L680,0 L0,0 Z" fill="var(--green-deep)"/>
    <path class="wave-band-dark" d="M0,440 C210,360 430,300 680,255 L680,330 C440,360 220,450 0,560 Z" fill="var(--green-deep)"/>
    <path class="wave-band-light" d="M0,520 C220,420 440,345 680,318 L680,340 C440,370 220,460 0,560 Z" fill="var(--green-bright)"/>
    <path class="content-area" d="M0,560 C220,470 440,380 680,345 L680,960 L0,960 Z" fill="var(--paper)"/>
    <path class="swoosh" d="M150,500 C300,420 470,300 680,265" fill="none" stroke="var(--orange)" stroke-width="6" stroke-linecap="round"/>

    <g class="lighting-photo" role="img" aria-label="Photo of garden path lights along a lawn edge at dusk">
      <polygon points="520,600 680,575 680,800 470,790" fill="url(#lightingSceneTone)"/>
    </g>

    <text class="brand-title" x="24" y="560">VERDAL</text>
    <g class="brand-mark">
      <circle cx="615" cy="482" r="30" fill="var(--orange)"/>
      <text class="brand-mark-name" x="560" y="530">VERDAL</text>
    </g>

    <text class="tagline" x="26" y="600">YOUR HANDS ARE FULL...LET US HELP</text>

    <g class="service-list">
      <g transform="translate(0,650)">
        <g class="service-icon" transform="translate(54,-9)"><circle r="11"/><path d="M-4,-6 L6,0 L-4,6 L-1,0 Z"/></g>
        <text class="service" x="78" y="0">FULL SERVICE</text>
      </g>
      <g transform="translate(0,690)">
        <g class="service-icon" transform="translate(54,-9)"><circle r="11"/><path d="M-4,-6 L6,0 L-4,6 L-1,0 Z"/></g>
        <text class="service" x="78" y="0">WEEKLY LAWN SERVICE</text>
      </g>
      <g transform="translate(0,730)">
        <g class="service-icon" transform="translate(54,-9)"><circle r="11"/><path d="M-4,-6 L6,0 L-4,6 L-1,0 Z"/></g>
        <text class="service" x="78" y="0">LANDSCAPE LIGHTING</text>
      </g>
      <g transform="translate(0,770)">
        <g class="service-icon" transform="translate(54,-9)"><circle r="11"/><path d="M-4,-6 L6,0 L-4,6 L-1,0 Z"/></g>
        <text class="service" x="78" y="0">SPRING/FALL CLEAN</text>
      </g>
      <g transform="translate(0,810)">
        <g class="service-icon" transform="translate(54,-9)"><circle r="11"/><path d="M-4,-6 L6,0 L-4,6 L-1,0 Z"/></g>
        <text class="service" x="78" y="0">TURF EDGING</text>
      </g>
      <g transform="translate(0,850)">
        <g class="service-icon" transform="translate(54,-9)"><circle r="11"/><path d="M-4,-6 L6,0 L-4,6 L-1,0 Z"/></g>
        <text class="service" x="78" y="0">SNOW REMOVAL</text>
      </g>
    </g>

    <path class="footer-edge" d="M330,872 C470,850 590,815 680,790 L680,800 C590,826 470,862 330,884 Z" fill="var(--orange)"/>
    <path class="footer-band" d="M0,880 C220,890 470,860 680,805 L680,960 L0,960 Z" fill="var(--green-deep)"/>
    <path class="footer-highlight" d="M0,880 C220,890 470,860 680,805 L680,815 C470,872 220,900 0,892 Z" fill="var(--green-mid)"/>

    <g class="footer-chevrons" fill="var(--orange)">
      <polygon points="240,866 300,880 240,894 250,880"/>
      <polygon points="262,866 322,880 262,894 272,880"/>
    </g>

    <text class="phone" x="26" y="940">(555) 214-3098</text>
    <text class="website" x="352" y="938">verdalquix.com</text>
  </svg>
</div>
</body>
</html>
```